Roaming outings business card

please see website
www.roamingoutings.comau

info needed on card
Keiran Voss
Ph
email
Adventure Riding GPS trails

please use my logo and colours off my site

Business

Keiran Voss
keiran@roamingoutings.com

```html
<!DOCTYPE html>
<html lang="en">
<head>
<meta charset="utf-8">
<title>Roaming Outings – Business Card</title>
<link href="https://fonts.googleapis.com/css2?family=Montserrat:wght@300;400;700&display=swap" rel="stylesheet">
<style>
  :root {
    --page-bg: #dcdcdc;
    --card-black: #0b0b0b;
    --card-charcoal: #1e1e1e;
    --photo-tone-a: #2c2c2c;
    --photo-tone-b: #121212;
    --brand-yellow: #f7cf1d;
    --text-white: #f4f4f4;
    --text-soft: #e2e2e2;
  }
  * { box-sizing: border-box; margin: 0; padding: 0; }
  html, body {
    width: 1200px; height: 1000px; overflow: hidden;
    background: var(--page-bg);
    font-family: "Montserrat", sans-serif;
  }
  .business-card {
    position: absolute; left: 100px; top: 222px;
    width: 1000px; height: 556px;
    background: radial-gradient(ellipse at 45% 35%, var(--card-charcoal) 0%, var(--card-black) 70%);
    overflow: hidden;
  }
  .rider-photo {
    position: absolute; left: 90px; top: 45px;
    width: 570px; height: 511px;
    background: radial-gradient(ellipse at 50% 55%, var(--photo-tone-a) 0%, var(--photo-tone-b) 60%, transparent 80%);
    opacity: 0.8;
  }
  .brand {
    position: absolute; left: 50px; top: 58px;
    display: flex; align-items: center; gap: 18px;
  }
  .brand-dot {
    width: 62px; height: 62px; border-radius: 50%;
    background: var(--brand-yellow);
  }
  .brand-name {
    color: var(--text-white);
    font-weight: 700; font-size: 30px; line-height: 1.05;
    text-transform: uppercase;
  }
  .tagline {
    position: absolute; right: 47px; top: 34px;
    text-align: right; color: var(--text-white);
    font-weight: 300; font-size: 47px; line-height: 56px;
  }
  .contact {
    position: absolute; right: 40px; top: 370px;
    text-align: right;
  }
  .contact-name {
    color: var(--brand-yellow);
    font-weight: 700; font-size: 38px; letter-spacing: 1px;
    text-transform: uppercase; margin-bottom: 6px;
  }
  .contact-line {
    display: flex; justify-content: flex-end; align-items: center; gap: 12px;
    color: var(--text-soft); font-size: 24px; font-weight: 400;
    height: 35px;
  }
  .contact-line svg { width: 24px; height: 24px; fill: var(--brand-yellow); }
</style>
</head>
<body>
  <section class="business-card">
    <div class="rider-photo" role="img" aria-label="Dark photo of an adventure rider on a dirt motorbike"></div>

    <div class="brand">
      <span class="brand-dot"></span>
      <span class="brand-name">Roaming<br>Outings</span>
    </div>

    <p class="tagline">Adventure<br>Riding GPS trails</p>

    <div class="contact">
      <p class="contact-name">Keiran Voss</p>
      <p class="contact-line">
        <svg viewBox="0 0 24 24" aria-hidden="true"><path d="M6.6 10.8a15.1 15.1 0 0 0 6.6 6.6l2.2-2.2a1 1 0 0 1 1-.25 11.4 11.4 0 0 0 3.6.57 1 1 0 0 1 1 1V20a1 1 0 0 1-1 1A17 17 0 0 1 3 4a1 1 0 0 1 1-1h3.5a1 1 0 0 1 1 1c0 1.25.2 2.45.57 3.57a1 1 0 0 1-.25 1z"/></svg>
        <span>+12 3456 7890</span>
      </p>
      <p class="contact-line">
        <svg viewBox="0 0 24 24" aria-hidden="true"><path d="M2 5h20v14H2z M2 5l10 8 10-8" stroke="#0b0b0b" stroke-width="1.5"/></svg>
        <span>keiran@roamingoutings.com</span>
      </p>
      <p class="contact-line">
        <svg viewBox="0 0 24 24" aria-hidden="true"><circle cx="12" cy="12" r="10"/><path d="M2 12h20M12 2c3 3 3 17 0 20M12 2c-3 3-3 17 0 20M4 7h16M4 17h16" stroke="#0b0b0b" stroke-width="1.3" fill="none"/></svg>
        <span>www.roamingoutings.com</span>
      </p>
    </div>
  </section>
</body>
</html>
```